Tariq Goldsmiths Stationary Contest

Pakistan’s largest Jewellery, Diamond and luxury watches store requires professional stationery. We have a long list of are trusted clients since 1959, our third generation has successfully maintained and sustained the legacy and excellence in the sector.

We require stationery template as part of this contest. The stationery can be double sided.

We prefer a design that makes use of some of the premium business stationery printing options, such as foil stamping, embossing/debossing, painted edges, spot UV etc (doesn't have to use all these options, only what you feel works, but we are looking for a design that stands out and is memorable and these nice touches have that effect.)

We want an eye catching, innovative, high end professional looking stationery for an out of box design that blends well with our new logo (attached). We want the design to be an out of box solution, you may use any element to compliment the logo. You may consider incorporating watermark etc, highlighting our products (Gold and Diamond Jewellery in addition to Luxury watches)

Company details are as follows;

Company name: Tariq Goldsmiths
Contact Person: Farhan Qureshi
Designation: Business Development Consultant
Mobile: +92 333 815 6042
Email: farhanqureshi@mailvale.com
Website: www.tariqgoldsmiths.com

Target Market(s)

Matrimonial, Elite & Businesses class, Upmarket

Font styles to use
Other font styles liked:
• Designers choice

Colors

Designer to choose colors to be used in the design.

Requirements
Must have
• Look and feel: Upmarket, innovative, Modern, Professional, graceful, Elegant, designer stuff.
Nice to have
• Unique design

```html
<!DOCTYPE html>
<html lang="en">
<head>
<meta charset="utf-8">
<title>Tariq Goldsmiths — Business Cards</title>
<link rel="stylesheet" href="https://fonts.googleapis.com/css2?family=Roboto:wght@400;500;700&display=swap">
<style>
  :root {
    --backdrop: #2b2522;
    --card-black: #1b1d21;
    --card-red-light: #c8173f;
    --card-red-dark: #9c0f2f;
    --gold: #e0a82e;
    --gold-edge: #b8862a;
    --white: #f4f1ec;
  }
  * { margin: 0; padding: 0; box-sizing: border-box; }
  html, body {
    width: 1200px; height: 769px; overflow: hidden;
    background: var(--backdrop);
    font-family: "Roboto", Arial, sans-serif;
  }
  .stage {
    position: relative; width: 1200px; height: 769px;
  }
  .card {
    position: absolute; top: 236px;
    width: 520px; height: 297px;
    border-bottom: 3px solid var(--gold-edge);
    box-shadow: 0 14px 30px rgba(0,0,0,0.45);
  }
  .card--front { left: 60px; background: var(--card-black); }
  .card--back {
    left: 620px;
    background: radial-gradient(ellipse at 40% 35%, var(--card-red-light), var(--card-red-dark));
  }
  .brand {
    position: absolute; left: 0; right: 0;
    display: flex; flex-direction: column; align-items: center; gap: 12px;
  }
  .card--front .brand { top: 62px; }
  .card--back .brand { top: 92px; }
  .brand__dot {
    width: 30px; height: 30px; border-radius: 50%;
    border: 2px solid var(--gold);
  }
  .brand__name {
    font-weight: 700; font-size: 26px; letter-spacing: 1px;
    text-transform: uppercase; color: var(--gold);
  }
  .contact {
    position: absolute; right: 28px; top: 170px;
    display: flex; flex-direction: column; align-items: flex-end; gap: 5px;
    color: var(--white); font-size: 13px;
  }
  .contact__row { display: flex; align-items: center; gap: 8px; }
  .contact__icon { width: 12px; height: 12px; }
  .person {
    position: absolute; left: 28px; bottom: 28px;
  }
  .person__name {
    color: var(--gold); font-weight: 700; font-size: 20px;
    text-transform: uppercase; letter-spacing: 0.3px;
  }
  .person__title { color: var(--white); font-size: 13px; margin-top: 3px; }
  .website {
    position: absolute; left: 0; right: 0; top: 200px; text-align: center;
    color: var(--white); font-size: 12px; letter-spacing: 3px;
  }
</style>
</head>
<body>
<main class="stage">
  <section class="card card--front">
    <div class="brand">
      <span class="brand__dot"></span>
      <span class="brand__name">Tariq Goldsmiths</span>
    </div>
    <div class="contact">
      <div class="contact__row">
        <span>+92 333 815 6042</span>
        <svg class="contact__icon" viewBox="0 0 12 12"><rect x="3" y="0.5" width="6" height="11" rx="1" fill="none" stroke="#e0a82e" stroke-width="1.2"/></svg>
      </div>
      <div class="contact__row">
        <span>farhanqureshi@mailvale.com</span>
        <svg class="contact__icon" viewBox="0 0 12 12"><rect x="0.5" y="2.5" width="11" height="7" fill="#e0a82e"/><path d="M0.5 2.5 L6 6.5 L11.5 2.5" fill="none" stroke="#1b1d21" stroke-width="1"/></svg>
      </div>
    </div>
    <div class="person">
      <div class="person__name">Farhan Qureshi</div>
      <div class="person__title">Business Development Consultant</div>
    </div>
  </section>

  <section class="card card--back">
    <div class="brand">
      <span class="brand__dot"></span>
      <span class="brand__name">Tariq Goldsmiths</span>
    </div>
    <div class="website">www.tariqgoldsmiths.com</div>
  </section>
</main>
</body>
</html>
```